Velmora Crest Fair - a fashion, art, design exhibition

Please see below. The poster must be very elegant. Eventhough it has an african name and feel, it should be modern and elegant so that it attracts all types of backgrounds and races to the show.

I want this poster to be so good that it attracts Sponsors, partners and exhibitors to want to be part of the show. So its my key marketing document.

Size: A0. Good luck and be creative!

Brief is below

The VELMORA CREST FAIR 2014

Dates: 19- 21 SEPTEMBER 2014:
all weekend event -open to the public
Time:
9am-5PM
OPEN TO THE PUBLIC
*Fashion shows will have exclusive show times

Venue to be confirmed

SHOWCASING
Fashion designers;
• Shoes designers;
• Accessory designers;
• Art;
• Cosmetics;
• Hair;
• Home and Décor;
• Media;
• Textiles and manufacturing;
• Technology;
• Tourism;
• Luxury/Lifestyle;
• Food & Others.

Countries representing:
SouthAfrica
Nigeria
Ghana
Kenya
Zimbabwe
Tanzania
Uganda
Ethiopia
Botswana
Mozambique
Zambia

To exhibit, partner or sponsor contact us:
Email: info@velmoracrestfair.com
Tele: 064 357 2816
Web: www.thevelmoracrestfair.com
Pagebook:/thevelmoracrestfair
Chirper:@the velmoracrestfair

All rights reserved. Presented by Trebiloe International

Please see the updated brief. I had alot of queries on the brief so i have shortened it.

Hi Designers,

I've attached our logo below. Please use logo version 2.1.3

We are interested in receiving more designs (right now there are only 2 to choose from)
Looking forward to your creativity.

Best regards

Hi all, Thanks for the designs that have been submitted. What i am really looking for is something that is elegant and catchy. The event/expo is an exhibition that will showcase, fashion, art, design, interior, comestics an hair etc. there will also be fashion shows that will be held on that day. It will be a nice classy event, that will draw crowds from all over Africa to participate. I have pasted the link below as a guide. Feel free to amend the brief or just use some of the info that will work. I need more designs. https://www.quorvexa.example/gallery/harvest-runway-posters/entry-4471

Target Market(s)

The public/ in SouthA frica, Africa and the world:
-Fashion bloggers
-Magazine Editors
-Fashion Brands
-Industry experts

those who attend will want to see:

- To interact and socialise with entrepreneurs
- See what’s new
- Evaluate products and suppliers
- Keep abreast of industry and market developments
- Network/develop business contacts
Solve specific problems
- Find new markets
- Appoint agents/seek principals
- Discuss specific terms/conditions/pricing
- Consolidate business relationships

It will be an all weekend event. Adults aged 25 as per above

Industry/Entity Type

Marketing

Font styles to use
Serif

Requirements
Must have
• The poster must be elegant and appealing
Nice to have
• Be creative, think, Harlowe Garment Days or Corvane style days and exhibition/trade fair combined.

The event will be fashion driven, so that lifestyle brands can also exhibit there
Should not have
• No old style

Not tacky

Must be classy

```html
<!DOCTYPE html>
<html lang="en">
<head>
<meta charset="utf-8">
<title>The Velmora Crest Fair 2014</title>
<link rel="stylesheet" href="https://fonts.googleapis.com/css2?family=Marcellus&family=Ubuntu:wght@400&display=swap">
<style>
  :root {
    --ink: #0b0b0b;
    --paper-text: #ffffff;
    --panel-text: #1c120a;
    --oxblood: #6e1a17;
    --rust: #9a3b24;
    --copper: #b86a35;
    --gold: #d6a24e;
    --body-font: "Ubuntu", sans-serif;
    --title-font: "Marcellus", serif;
  }
  * { margin: 0; padding: 0; box-sizing: border-box; }
  html, body { width: 1200px; height: 900px; overflow: hidden; background: var(--ink); }
  .poster {
    position: relative; width: 1200px; height: 900px;
    background: var(--ink); font-family: var(--body-font); color: var(--paper-text);
  }
  .frame {
    position: absolute; left: 38px; top: 32px; width: 1125px; height: 835px;
    border: 6px solid transparent;
    border-image: linear-gradient(90deg, var(--oxblood), var(--gold) 40%, var(--copper) 70%, var(--oxblood)) 1;
  }
  .panel-fill {
    background: linear-gradient(90deg, var(--oxblood) 0%, var(--copper) 25%, var(--gold) 55%, var(--copper) 80%, var(--rust) 100%);
  }
  .showcase-heading {
    position: absolute; left: 65px; top: 117px; width: 375px; height: 50px;
    color: var(--panel-text); font-size: 25px; padding: 16px 0 0 19px; letter-spacing: 0.5px;
  }
  .showcase-list {
    position: absolute; left: 65px; top: 175px; width: 375px; height: 607px;
    list-style: none; padding: 4px 0 0 19px; color: var(--panel-text);
  }
  .showcase-list li { font-size: 26px; line-height: 46.3px; white-space: nowrap; }
  .details-band {
    position: absolute; left: 470px; top: 76px; width: 592px; height: 122px;
    background: linear-gradient(90deg, rgba(0,0,0,0) 0%, var(--oxblood) 10%, var(--rust) 30%, var(--gold) 55%, var(--copper) 75%, rgba(110,26,23,0.6) 92%, rgba(0,0,0,0) 100%);
  }
  .event-dates { position: absolute; left: 0; top: 10px; width: 610px; text-align: center; font-size: 26px; }
  .event-note { position: absolute; left: 0; top: 50px; width: 600px; text-align: center; font-size: 21px; }
  .event-time { position: absolute; left: 8px; top: 88px; font-size: 25px; }
  .event-venue { position: absolute; left: 278px; top: 93px; font-size: 20px; }
  .map-artwork { position: absolute; left: 740px; top: 235px; width: 400px; height: 380px; }
  .event-title {
    position: absolute; left: 548px; top: 412px; width: 360px;
    font-family: var(--title-font); font-weight: 400; color: var(--paper-text);
    line-height: 1; text-align: right;
  }
  .event-title .title-line { display: block; white-space: nowrap; }
  .title-lead { font-size: 52px; text-align: left; }
  .title-main { font-size: 54px; margin-top: 14px; }
  .title-year { font-size: 62px; margin-top: 12px; padding-right: 10px; }
  .contact-band {
    position: absolute; left: 512px; top: 640px; width: 565px; height: 30px;
    background: linear-gradient(90deg, rgba(0,0,0,0) 0%, var(--oxblood) 12%, var(--copper) 45%, var(--gold) 60%, var(--rust) 88%, rgba(0,0,0,0) 100%);
    text-align: center; font-size: 20px; line-height: 31px;
  }
  .contact-list {
    position: absolute; left: 600px; top: 690px; width: 400px;
    list-style: none; text-align: center; font-size: 20px; line-height: 28.6px;
  }
  .footer-credit { position: absolute; left: 38px; top: 874px; font-size: 14px; }
  .footer-note { position: absolute; right: 40px; top: 874px; font-size: 14px; }
</style>
</head>
<body>
<main class="poster">
  <div class="frame"></div>

  <h2 class="showcase-heading panel-fill">SHOWCASING</h2>
  <ul class="showcase-list panel-fill">
    <li>Fashion designers</li>
    <li>Shoes designers</li>
    <li>Accessory designers</li>
    <li>Art</li>
    <li>Cosmetics</li>
    <li>Hair</li>
    <li>Home and Décor</li>
    <li>Media</li>
    <li>Textiles and manufacturing</li>
    <li>Technology</li>
    <li>Tourism</li>
    <li>Luxury/Lifestyle</li>
    <li>Food &amp; Others.</li>
  </ul>

  <section class="details-band">
    <p class="event-dates">Dates: 19- 21 SEPTEMBER 2014</p>
    <p class="event-note">All weekend event -open to the public</p>
    <p class="event-time">Time : 9am-5PM</p>
    <p class="event-venue">Venue :</p>
  </section>

  <svg class="map-artwork" viewBox="0 0 400 380" role="img" aria-label="Striped continent map artwork in copper and gold tones">
    <defs>
      <linearGradient id="mapTone" x1="0" y1="0" x2="1" y2="0">
        <stop offset="0" stop-color="#6e1a17"/>
        <stop offset="0.45" stop-color="#d6a24e"/>
        <stop offset="0.8" stop-color="#b86a35"/>
        <stop offset="1" stop-color="#8a2f1f"/>
      </linearGradient>
    </defs>
    <rect x="20" y="10" width="370" height="360" rx="150" fill="url(#mapTone)" opacity="0.85"/>
  </svg>

  <h1 class="event-title">
    <span class="title-line title-lead">The VELMORA</span>
    <span class="title-line title-main">CREST FAIR</span>
    <span class="title-line title-year">2014</span>
  </h1>

  <p class="contact-band">To exhibit, partner or sponsor contact us:</p>
  <ul class="contact-list">
    <li>Email: info@velmoracrestfair.com</li>
    <li>Tele: 064 357 2816</li>
    <li>Web: www.thevelmoracrestfair.com</li>
    <li>Pagebook:/thevelmoracrestfair</li>
    <li>Chirper:@the velmoracrestfair</li>
  </ul>

  <p class="footer-credit">All rights reserved. Presented by Trebiloe International:</p>
  <p class="footer-note">*Fashion shows will have exclusive show times</p>
</main>
</body>
</html>
```